Tarvel Works - Powerpoint Templates

We are a consultancy to help builders to optimize their planning in order to save building costs. For that reason we need templates for teasers and presentations where we offer our services, show our team and their capacities and present workflows, organization charts, price lists etc.

```html
<!DOCTYPE html>
<html lang="en">
<head>
<meta charset="utf-8">
<title>Tarvel Works – Presentation Template</title>
<link href="https://fonts.googleapis.com/css2?family=Open+Sans:wght@300;400;600;700&display=swap" rel="stylesheet">
<style>
:root{
  --page:#ffffff;
  --board:#e5e5e5;
  --ink:#1c1c1c;
  --ink-soft:#262626;
  --gold:#f2b705;
  --gold-mid:#d99c00;
  --gold-deep:#7a5600;
  --white:#ffffff;
  --muted:#b5b5b5;
  --cream:#f3e6c4;
  --steel:#8c8c8c;
}
*{margin:0;padding:0;box-sizing:border-box}
html,body{width:1200px;height:1200px;overflow:hidden;background:var(--page)}
body{font-family:"Open Sans",Arial,sans-serif;color:var(--white);position:relative}
.board{position:absolute;left:386px;top:0;width:428px;height:1200px;background:var(--board)}
.slide{position:absolute;width:621px;height:354px;background:var(--ink);overflow:hidden;transform-origin:0 0;transform:scale(.3333)}
.slide.hero{transform:scale(.644)}
.slide *{position:absolute}
.slide .flow,.slide .flow *{position:static}
.meta{left:40px;right:40px;top:14px;display:flex;justify-content:space-between;font-size:6px;color:var(--white)}
.meta span{position:static}
.brand-mini{right:22px;bottom:10px;font-size:6px;font-weight:600;color:var(--gold);display:flex;align-items:center;gap:3px}
.brand-mini i{position:static;display:block;width:6px;height:6px;background:var(--gold)}
.photo{display:block}
.ph-grey{background:linear-gradient(160deg,#e9e9e9,#9a9a9a 55%,#3a3a3a)}
.ph-light{background:linear-gradient(150deg,#f4f4f4,#cfcfcf 60%,#8e8e8e)}
.ph-sky{background:linear-gradient(180deg,#5aa9e6,#9fd0f2 60%,#d7ecf8)}
.ph-warm{background:linear-gradient(150deg,#b9b9b9,#8b8b8b 50%,#d58a22)}
.ph-hat{background:linear-gradient(170deg,#eef1f4,#d4dbe2 55%,#e8b400 80%,#cfcfcf)}
.ph-blue{background:linear-gradient(160deg,#cfd6de,#7b8fa8 50%,#2e3f58)}
.gold-v{background:linear-gradient(180deg,var(--gold),var(--gold-mid) 55%,var(--ink))}
.gold-h{background:linear-gradient(90deg,var(--gold),var(--gold-mid) 65%,var(--ink))}
.gold-rise{background:linear-gradient(0deg,var(--gold),var(--gold-deep) 60%,var(--ink))}
.h-title{font-weight:700;color:var(--white);line-height:1.3;text-transform:uppercase}
.h-gold{color:var(--gold);font-weight:400;line-height:1.25;text-transform:uppercase}
.body{font-size:6px;line-height:1.7;color:var(--muted)}
.body.w{color:var(--white)}
.rule{height:1px;background:#5a4a1e}
.vrule{width:1px;background:#5a4a1e}
.dot{width:5px;height:5px;border-radius:50%;background:var(--gold)}
.stat{font-size:34px;font-weight:300;color:var(--white)}
.frame{fill:none;stroke:var(--gold-mid);stroke-width:1}
.brand{display:flex;align-items:center;gap:8px;font-weight:600;color:var(--gold)}
.brand i{position:static;display:block;width:16px;height:16px;background:var(--gold)}
.card-name{font-size:7px;color:var(--white);text-align:center;width:100%}
.icon{stroke:var(--gold);fill:none;stroke-width:1.4}
</style>
</head>
<body>
<div class="board"></div>

<!-- Title slide (large preview) -->
<section class="slide hero" style="left:400px;top:40px">
  <div class="meta"><span>Tarvel Works</span><span>BUSINESS</span><span>2023</span></div>
  <div class="photo ph-grey" role="img" aria-label="Tower under construction with cranes" style="left:26px;top:84px;width:207px;height:252px"></div>
  <div style="left:265px;top:86px;font-size:9px">BUSINESS PLAN</div>
  <div class="rule" style="left:360px;top:93px;width:235px"></div>
  <div class="brand" style="left:265px;top:136px;font-size:16px"><i></i>Tarvel Works</div>
  <div style="left:263px;top:176px;font-size:46px;font-weight:400;line-height:1.2;white-space:nowrap"><span class="flow" style="color:var(--gold)">TARVEL</span> <span class="flow">WORKS</span></div>
  <div style="left:270px;top:243px;font-size:10px;color:var(--muted)">We offer a range of services to help you plan your projects better.</div>
  <div style="left:256px;top:323px;font-size:7px">@Tarvel Works</div>
  <div class="rule" style="left:310px;top:327px;width:55px;background:var(--gold-mid)"></div>
  <svg width="90" height="90" style="left:531px;top:264px"><path class="frame" d="M10 90V12H90M22 90V24H90M34 90V36H78V90M46 90V48H66V90"/></svg>
</section>

<!-- Row 1 -->
<section class="slide" style="left:390px;top:313px">
  <div class="meta"><span>Tarvel Works</span><span>BUSINESS</span><span>2023</span></div>
  <div class="photo ph-grey" role="img" aria-label="Tower under construction with cranes" style="left:26px;top:84px;width:207px;height:252px"></div>
  <div style="left:265px;top:86px;font-size:9px">BUSINESS PLAN</div>
  <div class="rule" style="left:360px;top:93px;width:235px"></div>
  <div class="brand" style="left:265px;top:136px;font-size:16px"><i></i>Tarvel Works</div>
  <div style="left:263px;top:176px;font-size:46px;font-weight:400;line-height:1.2;white-space:nowrap"><span class="flow" style="color:var(--gold)">TARVEL</span> <span class="flow">WORKS</span></div>
  <div style="left:270px;top:243px;font-size:10px;color:var(--muted)">We offer a range of services to help you plan your projects better.</div>
  <div style="left:256px;top:323px;font-size:7px">@Tarvel Works</div>
  <div class="rule" style="left:310px;top:327px;width:55px;background:var(--gold-mid)"></div>
  <svg width="90" height="90" style="left:531px;top:264px"><path class="frame" d="M10 90V12H90M22 90V24H90M34 90V36H78V90M46 90V48H66V90"/></svg>
</section>

<section class="slide" style="left:601px;top:313px">
  <div class="gold-h" style="left:24px;top:19px;width:350px;height:37px"></div>
  <div class="meta" style="left:40px;right:260px;top:34px"><span>Tarvel Works</span><span>BUSINESS</span><span>2023</span></div>
  <div class="gold-v" style="left:373px;top:19px;width:229px;height:317px"></div>
  <div class="photo ph-hat" role="img" aria-label="Yellow hard hat, calculator and building plans" style="left:401px;top:52px;width:168px;height:256px"></div>
  <div class="h-title" style="left:58px;top:86px;font-size:21px">How to plan<br>your construction<br>projects</div>
  <div class="body w" style="left:58px;top:186px;width:260px">If you are a builder, you know how important it is to plan your projects carefully and efficiently. You want high-quality work, meet deadlines and stay within budget.</div>
  <div class="dot" style="left:52px;top:236px;width:18px;height:18px"></div>
  <div style="left:78px;top:238px;font-size:7px">Efficiently</div>
  <div class="body w" style="left:78px;top:256px;width:110px">You want to deliver high-quality work, meet deadlines and stay within budget.</div>
  <div class="dot" style="left:206px;top:236px;width:18px;height:18px"></div>
  <div style="left:232px;top:238px;font-size:7px">Effectively</div>
  <div class="body w" style="left:232px;top:256px;width:120px">Materials availability, regulations, design changes and customer expectations.</div>
  <div class="brand-mini"><i></i>Tarvel Works</div>
</section>

<!-- Row 2 -->
<section class="slide" style="left:390px;top:440px">
  <div class="photo ph-blue" role="img" aria-label="Handshake between two builders" style="left:26px;top:19px;width:201px;height:153px"></div>
  <div class="photo ph-light" role="img" aria-label="Two engineers reviewing plans on site" style="left:26px;top:183px;width:201px;height:153px"></div>
  <div class="gold-h" style="left:250px;top:19px;width:343px;height:97px"></div>
  <div class="h-title" style="left:280px;top:43px;font-size:18px">The benefits of optimizing<br>your building costs</div>
  <div class="gold-v" style="left:250px;top:123px;width:24px;height:213px;background:linear-gradient(0deg,var(--gold),var(--gold-mid) 60%,var(--ink))"></div>
  <div class="stat" style="left:318px;top:132px">83+</div>
  <div style="left:318px;top:180px;font-size:6px;width:70px;text-align:center">Quality control</div>
  <div class="stat" style="left:438px;top:132px">$540</div>
  <div style="left:440px;top:180px;font-size:6px;width:80px;text-align:center">Cost estimation and budgeting</div>
  <div class="body w" style="left:300px;top:220px;width:270px">That's why you need a consultancy that can help you optimize your planning and save building costs, with the expertise, tools and experience to analyse your requirements.</div>
  <div class="body w" style="left:300px;top:272px;width:240px">At Tarvel Works we offer a range of services to help you plan your projects better.</div>
  <svg width="20" height="60" style="left:583px;top:165px"><path class="frame" d="M2 0V60M7 0V60M12 0V60"/></svg>
  <div class="brand-mini"><i></i>Tarvel Works</div>
</section>

<section class="slide" style="left:601px;top:440px">
  <div class="meta"><span>Tarvel Works</span><span>BUSINESS</span><span>2023</span></div>
  <div class="h-title" style="left:54px;top:76px;font-size:26px">About us</div>
  <div class="rule" style="left:54px;top:130px;width:256px"></div>
  <div class="photo ph-light" role="img" aria-label="Modern glass office building facade" style="left:321px;top:88px;width:276px;height:150px"></div>
  <div class="gold-rise" style="left:321px;top:238px;width:276px;height:34px;background:linear-gradient(180deg,var(--gold),var(--ink))"></div>
  <div class="body w" style="left:54px;top:160px;width:200px">At Tarvel Works we offer a range of services to help you plan your projects better. We can help you with:</div>
  <div class="flow" style="position:absolute;left:54px;top:220px;font-size:6.5px;line-height:20px">
    <div style="display:flex;align-items:center;gap:8px"><span class="dot" style="display:block;position:static"></span>Site assessment and feasibility studies</div>
    <div style="display:flex;align-items:center;gap:8px"><span class="dot" style="display:block;position:static"></span>Cost estimation and budgeting</div>
    <div style="display:flex;align-items:center;gap:8px"><span class="dot" style="display:block;position:static"></span>Scheduling and resource allocation</div>
    <div style="display:flex;align-items:center;gap:8px"><span class="dot" style="display:block;position:static"></span>Risk management and mitigation</div>
    <div style="display:flex;align-items:center;gap:8px"><span class="dot" style="display:block;position:static"></span>Quality control and assurance</div>
  </div>
  <svg width="30" height="60" style="left:0;top:180px"><path class="frame" d="M4 0V60M10 0V60M16 0V60M22 0V60"/></svg>
  <div class="brand-mini"><i></i>Tarvel Works</div>
</section>

<!-- Row 3 -->
<section class="slide" style="left:390px;top:566px">
  <div class="meta"><span>Tarvel Works</span><span></span><span>2023</span></div>
  <div class="h-title" style="left:41px;top:58px;font-size:21px">Successful<br>case studies</div>
  <svg width="20" height="22" style="left:41px;top:162px"><path class="icon" d="M10 1L18 4V11C18 16 14 19 10 21C6 19 2 16 2 11V4Z"/></svg>
  <div class="body w" style="left:41px;top:194px;width:180px">That's why you need a consultancy that can help you optimize your planning and save building costs, with the expertise and tools to analyse your requirements and identify risks.</div>
  <div class="body w" style="left:41px;top:266px;width:160px">At Tarvel Works we offer a range of services to help you plan better.</div>
  <div class="photo ph-sky" role="img" aria-label="Tower crane against a blue sky" style="left:254px;top:19px;width:114px;height:317px"></div>
  <div class="dot" style="left:400px;top:59px"></div>
  <div style="left:412px;top:56px;font-size:7px">Site assessment</div>
  <div class="body w" style="left:412px;top:72px;width:160px">Clear review of the plot, access and soil before design work starts.</div>
  <div class="rule" style="left:400px;top:140px;width:180px"></div>
  <div class="dot" style="left:400px;top:167px"></div>
  <div style="left:412px;top:164px;font-size:7px">Cost estimation</div>
  <div class="body w" style="left:412px;top:180px;width:160px">Reliable budgets built from quantities, rates and market prices.</div>
  <div class="rule" style="left:400px;top:245px;width:180px"></div>
  <div class="dot" style="left:400px;top:269px"></div>
  <div style="left:412px;top:266px;font-size:7px">Scheduling and resource allocation</div>
  <div class="body w" style="left:412px;top:282px;width:160px">Realistic timelines that keep crews and materials on track.</div>
  <div class="brand-mini"><i></i>Tarvel Works</div>
</section>

<section class="slide" style="left:601px;top:566px">
  <div class="meta"><span>Tarvel Works</span><span>BUSINESS</span><span>2023</span></div>
  <div class="h-title" style="left:50px;top:52px;font-size:21px">The benefits of<br>optimizing your<br>building costs</div>
  <div class="body w" style="left:50px;top:155px;width:220px">If you are a builder, you know how important it is to plan your projects carefully and efficiently, deliver quality work and stay within budget.</div>
  <svg width="290" height="170" style="left:318px;top:50px"><path class="frame" d="M0 20V150M280 0V140"/></svg>
  <div class="photo ph-light" role="img" aria-label="Engineers working with laptop and hard hat at a desk" style="left:330px;top:56px;width:267px;height:159px"></div>
  <div style="left:32px;top:237px;width:293px;height:99px;background:linear-gradient(90deg,var(--gold-deep),var(--gold))"></div>
  <div class="stat" style="left:65px;top:262px;font-size:36px">83+</div>
  <div style="left:150px;top:276px;font-size:5px;width:120px;line-height:1.6">Successful case studies of optimized construction projects</div>
  <div style="left:340px;top:239px;width:257px;height:14px;background:var(--gold);font-size:5px;letter-spacing:3px;text-align:center;line-height:14px">TARVEL WORKS</div>
  <div class="body w" style="left:366px;top:266px;width:200px">That's why you need a consultancy that can help you optimize your planning and save building costs.</div>
  <div class="brand-mini"><i></i>Tarvel Works</div>
</section>

<!-- Row 4 -->
<section class="slide" style="left:390px;top:690px">
  <div class="meta"><span>Tarvel Works</span><span>BUSINESS</span><span>2023</span></div>
  <svg width="20" height="240" style="left:6px;top:90px"><path class="frame" d="M4 0V240M10 20V240M16 40V240"/></svg>
  <div class="photo ph-warm" role="img" aria-label="Construction workers in safety vests on site" style="left:48px;top:56px;width:185px;height:130px"></div>
  <div style="left:48px;top:186px;width:185px;height:104px;background:linear-gradient(180deg,var(--gold-mid),var(--gold-deep) 70%,var(--ink))"></div>
  <div style="left:78px;top:196px;font-size:7px;line-height:1.4">Site assessment and<br>feasibility studies</div>
  <div class="body w" style="left:60px;top:228px;width:160px;text-align:center">That's why you need a consultancy that can help you plan and save building costs.</div>
  <div class="h-title" style="left:260px;top:88px;font-size:18px;font-weight:600">Avoid common pitfalls<br>and risks in construction</div>
  <div class="body w" style="left:290px;top:200px;width:250px;text-align:right">That's why you need a consultancy that can help you optimize your planning and save building costs, with the expertise, tools and experience to find potential risks early.<br><b style="font-weight:700">At Tarvel Works we offer a range of services to help you plan your projects better.</b></div>
  <div style="left:55px;top:325px;font-size:6px">@Tarvel Works</div>
  <div class="rule" style="left:105px;top:328px;width:55px;background:var(--gold-mid)"></div>
  <div class="brand-mini"><i></i>Tarvel Works</div>
</section>

<section class="slide" style="left:601px;top:690px">
  <div class="meta"><span>Tarvel Works</span><span>BUSINESS</span><span>2023</span></div>
  <svg width="70" height="60" style="left:540px;top:0"><path class="frame" d="M10 60V12H70M22 60V24H70M34 60V36H70"/></svg>
  <div class="h-gold" style="left:37px;top:66px;font-size:32px">Our<br>mission</div>
  <div style="left:237px;top:71px;width:168px;height:209px;background:linear-gradient(180deg,var(--gold-mid),var(--gold-deep) 75%,var(--ink))"></div>
  <svg width="16" height="18" style="left:313px;top:86px"><path class="icon" d="M8 1L15 4V9C15 13 12 16 8 17C4 16 1 13 1 9V4Z" style="stroke:var(--white)"/></svg>
  <div class="body w" style="left:250px;top:110px;width:142px;text-align:center">Plan smarter, build leaner and protect every client budget.</div>
  <svg width="16" height="18" style="left:313px;top:190px"><rect class="icon" x="2" y="1" width="12" height="16" style="stroke:var(--white)"/></svg>
  <div class="body w" style="left:250px;top:214px;width:142px;text-align:center">Clear advice from the first sketch to final handover.</div>
  <div class="photo ph-light" role="img" aria-label="Two people reviewing documents at a desk" style="left:405px;top:71px;width:196px;height:209px"></div>
  <div class="body w" style="left:37px;top:190px;width:170px">We guide builders through every phase, cutting waste and keeping projects on schedule and within budget.</div>
  <div style="left:32px;top:280px;width:46px;height:41px;background:var(--gold);font-size:11px;text-align:center;line-height:41px">75%</div>
  <div style="left:88px;top:282px;font-size:5.5px;font-weight:700;line-height:1.7">Average savings in planning<br>time across our projects.<br>Proven results.</div>
  <div style="left:257px;top:325px;font-size:6px">@Tarvel Works</div>
  <div class="brand-mini"><i></i>Tarvel Works</div>
</section>

<!-- Row 5 -->
<section class="slide" style="left:390px;top:816px">
  <div class="meta"><span>Tarvel Works</span><span>BUSINESS</span><span>2023</span></div>
  <svg width="140" height="150" style="left:470px;top:40px"><path class="frame" d="M10 150V10H140M22 150V22H128V150M34 150V34H116V150"/></svg>
  <div class="h-title" style="left:39px;top:46px;font-size:32px;font-weight:600;line-height:1.4">Our<br>vision</div>
  <div class="rule" style="left:39px;top:150px;width:203px"></div>
  <div class="body w" style="left:245px;top:108px;width:210px">That's why you need a consultancy that can help you optimize your planning and save building costs.</div>
  <div class="gold-h" style="left:242px;top:149px;width:355px;height:22px"></div>
  <div class="photo ph-hat" role="img" aria-label="Yellow hard hat and rolled plans before a city skyline" style="left:242px;top:171px;width:355px;height:170px"></div>
  <div style="left:39px;top:209px;font-size:6px">THE VISION</div>
  <div class="body w" style="left:39px;top:240px;width:160px;font-size:7px">If you are a builder, you know how important it is to plan your projects carefully and efficiently.</div>
  <div style="left:0;top:280px;width:24px;height:74px;background:var(--gold)"></div>
</section>

<section class="slide" style="left:601px;top:816px">
  <div class="meta"><span>Tarvel Works</span><span>BUSINESS</span><span>2023</span></div>
  <svg width="621" height="354" style="left:0;top:0"><path class="frame" d="M30 300V110H42M590 300V110H578M20 310V100M600 310V100"/></svg>
  <div class="h-title" style="left:0;width:621px;text-align:center;top:72px;font-size:28px;font-weight:600">Our team</div>
  <div class="photo ph-light" role="img" aria-label="Portrait of team member Mara Lind" style="left:52px;top:129px;width:157px;height:108px"></div>
  <div class="photo ph-light" role="img" aria-label="Portrait of team member Jana Lowe" style="left:237px;top:129px;width:157px;height:108px"></div>
  <div class="photo ph-light" role="img" aria-label="Portrait of team member Rico Laval" style="left:422px;top:129px;width:157px;height:108px"></div>
  <div style="left:52px;top:237px;width:157px;height:63px;background:linear-gradient(180deg,var(--gold-mid),var(--gold-deep) 70%,var(--ink))"><div class="card-name" style="top:10px">MARA LIND</div><div class="body w" style="top:24px;width:100%;text-align:center;font-size:5px">Cost planning lead,<br>budgets and tenders</div></div>
  <div style="left:237px;top:237px;width:157px;height:63px;background:linear-gradient(180deg,var(--gold-mid),var(--gold-deep) 70%,var(--ink))"><div class="card-name" style="top:10px">JANA LOWE</div><div class="body w" style="top:24px;width:100%;text-align:center;font-size:5px">Scheduling expert,<br>site coordination</div></div>
  <div style="left:422px;top:237px;width:157px;height:63px;background:linear-gradient(180deg,var(--gold-mid),var(--gold-deep) 70%,var(--ink))"><div class="card-name" style="top:10px">RICO LAVAL</div><div class="body w" style="top:24px;width:100%;text-align:center;font-size:5px">Risk and quality,<br>contract review</div></div>
  <div style="left:0;width:621px;text-align:center;top:331px;font-size:6px">@Tarvel Works</div>
  <div class="brand-mini"><i></i>Tarvel Works</div>
</section>

<!-- Row 6 -->
<section class="slide" style="left:390px;top:942px">
  <div class="meta"><span>Tarvel Works</span><span>BUSINESS</span><span>2023</span></div>
  <div class="brand" style="left:41px;top:56px;font-size:6px;gap:3px"><i style="width:6px;height:6px"></i>Tarvel Works</div>
  <div class="h-title" style="left:236px;top:44px;font-size:30px;font-weight:600;line-height:1.35">Our<br>service</div>
  <div class="rule" style="left:380px;top:118px;width:55px;background:var(--gold-mid)"></div>
  <div style="left:440px;top:114px;font-size:6px">@Tarvel Works</div>
  <div class="rule" style="left:236px;top:140px;width:361px"></div>
  <div class="gold-h" style="left:26px;top:88px;width:179px;height:52px"></div>
  <div class="photo ph-light" role="img" aria-label="Businesswoman shaking hands with a builder in a hard hat" style="left:26px;top:140px;width:179px;height:196px"></div>
  <svg width="600" height="100" style="left:0;top:240px"><path class="frame" d="M10 0V100M20 20V100"/></svg>
  <svg width="20" height="22" style="left:233px;top:168px"><path class="icon" d="M10 1L18 4V11C18 16 14 19 10 21C6 19 2 16 2 11V4Z"/></svg>
  <div style="left:275px;top:168px;font-size:6.5px">Smart Planning Strategies</div>
  <div class="body w" style="left:275px;top:182px;width:120px">Sharper plans that cut waste and keep work moving.</div>
  <svg width="22" height="22" style="left:423px;top:166px"><path class="icon" d="M5 2H17V8C17 12 14 14 11 14C8 14 5 12 5 8ZM5 4H1C1 8 3 9 5 9M17 4H21C21 8 19 9 17 9M11 14V18M6 21H16"/></svg>
  <div style="left:467px;top:168px;font-size:6.5px">Construction Planning and<br>Management</div>
  <div class="body w" style="left:467px;top:190px;width:120px">Full control of scope, schedule and cost.</div>
  <svg width="22" height="24" style="left:233px;top:266px"><circle class="icon" cx="11" cy="9" r="7"/><path class="icon" d="M6 15L4 23L11 19L18 23L16 15"/></svg>
  <div style="left:275px;top:268px;font-size:6.5px">Optimized Construction<br>Projects</div>
  <div class="body w" style="left:275px;top:290px;width:120px">Lean processes for better results.</div>
  <svg width="20" height="24" style="left:423px;top:266px"><rect class="icon" x="2" y="3" width="16" height="20"/><path class="icon" d="M6 10H14M6 15H14M7 1H13V5H7Z"/></svg>
  <div style="left:467px;top:268px;font-size:6.5px">Projects Efficiently and<br>Effectively</div>
  <div class="body w" style="left:467px;top:290px;width:120px">Delivered on time and on budget.</div>
</section>

<section class="slide" style="left:601px;top:942px">
  <div class="meta"><span>Tarvel Works</span><span>BUSINESS</span><span>2023</span></div>
  <div class="h-gold" style="left:62px;top:44px;font-size:22px">Company<br>data chart</div>
  <div class="vrule" style="left:232px;top:50px;height:48px;background:var(--gold)"></div>
  <div class="body w" style="left:273px;top:48px;width:290px">We track planning time, savings and delivery rates across every project so clients can see where their budget works hardest. Data drives each decision we recommend.</div>
  <svg width="540" height="160" style="left:40px;top:118px" role="img" aria-label="Bar chart of company results in four groups">
    <g stroke="#555" stroke-width="0.6">
      <line x1="30" y1="145" x2="530" y2="145"/><line x1="30" y1="122.5" x2="530" y2="122.5"/><line x1="30" y1="100" x2="530" y2="100"/><line x1="30" y1="77.5" x2="530" y2="77.5"/><line x1="30" y1="55" x2="530" y2="55"/><line x1="30" y1="32.5" x2="530" y2="32.5"/><line x1="30" y1="10" x2="530" y2="10"/>
    </g>
    <g fill="#ffffff" font-size="7" font-family="Open Sans, sans-serif" text-anchor="end">
      <text x="22" y="148">0</text><text x="22" y="125">1</text><text x="22" y="103">2</text><text x="22" y="80">3</text><text x="22" y="58">4</text><text x="22" y="35">5</text><text x="22" y="13">6</text>
    </g>
    <rect x="70" y="48" width="20" height="97" fill="var(--steel)"/><rect x="95" y="93" width="20" height="52" fill="var(--cream)"/><rect x="120" y="100" width="20" height="45" fill="var(--gold)"/>
    <rect x="195" y="91" width="20" height="54" fill="var(--steel)"/><rect x="220" y="48" width="20" height="97" fill="var(--cream)"/><rect x="245" y="100" width="20" height="45" fill="var(--gold)"/>
    <rect x="320" y="66" width="20" height="79" fill="var(--steel)"/><rect x="345" y="105" width="20" height="40" fill="var(--cream)"/><rect x="370" y="78" width="20" height="67" fill="var(--gold)"/>
    <rect x="445" y="44" width="20" height="101" fill="var(--steel)"/><rect x="470" y="82" width="20" height="63" fill="var(--cream)"/><rect x="495" y="33" width="20" height="112" fill="var(--gold)"/>
  </svg>
  <div class="body w" style="left:54px;top:294px;width:300px">Figures show yearly averages for planning hours, cost savings and on-time delivery per project type.</div>
  <div class="brand-mini"><i></i>Tarvel Works</div>
</section>

<!-- Row 7 -->
<section class="slide" style="left:390px;top:1068px">
  <div style="left:0;top:0;width:24px;height:354px;background:linear-gradient(180deg,var(--ink),var(--gold-deep) 40%,var(--gold))"></div>
  <div class="meta" style="left:52px;right:330px"><span>Tarvel Works</span><span>BUSINESS</span><span>2023</span></div>
  <div class="h-gold" style="left:63px;top:158px;font-size:34px">Thank you!</div>
  <div style="left:120px;top:204px;font-size:6px">FOR YOUR ATTENTION</div>
  <div class="photo ph-light" role="img" aria-label="Handshake over construction plans and a hard hat" style="left:305px;top:19px;width:291px;height:317px"></div>
  <svg width="621" height="354" style="left:0;top:0"><path class="frame" d="M250 354V300H305M262 354V312H305M40 336H300M596 336H621"/></svg>
  <div style="left:120px;top:320px;font-size:6px">@Tarvel Works</div>
</section>
</body>
</html>
```